Poster Required for Cafe to promote Catering

I would like a Poster made to advertise that our business does catering.
On the poster we would like it to say:

Did you know that Sunny Ladle does Catering?
We offer Breakfast, Lunch, Morning and Afternoon Tea Options
Come instore to enquire

At the bottom of the flyer, can you please put the contact details:
Phone 0487 602 914
Email tam@sunnyladlecanteen.com

Poster Size A3

I have attached our logo and menu's so you can get a feel for what we like.

Target Market(s)

Hospital Staff: Doctors, Nurses, Admin

Industry/Entity Type

Hospitality

Requirements
Nice to have
• Some pictures of catering. Eg. Gourmet Sandwiches, Sliders
• You could check our instagram page for ideas on what we do..
• @snyladle_qld

```html
<!DOCTYPE html>
<html lang="en">
<head>
<meta charset="utf-8">
<title>Sunny Ladle Catering Poster</title>
<link rel="stylesheet" href="https://fonts.googleapis.com/css2?family=League+Gothic&family=Roboto+Condensed:wght@700&family=Roboto:wght@300&display=swap">
<style>
  :root {
    --paper: #fff8a4;
    --ink: #3b3131;
    --ink-soft: rgba(59, 49, 49, 0.14);
    --ink-faint: rgba(59, 49, 49, 0.04);
    --logo-text: #d9d3cf;
  }
  * { margin: 0; padding: 0; box-sizing: border-box; }
  html, body { width: 849px; height: 1200px; overflow: hidden; }
  body { background: var(--paper); color: var(--ink); position: relative; }

  .headline {
    position: absolute;
    left: 108px;
    font-family: "League Gothic", "Oswald", sans-serif;
    font-weight: 400;
    text-transform: uppercase;
    line-height: 0.78;
    white-space: nowrap;
    transform-origin: left top;
    font-size: 150px;
  }
  .headline--intro { top: 112px; transform: scaleX(0.72); }
  .headline--intro .line { display: block; margin-bottom: 6px; }
  .headline--offer { top: 550px; transform: scaleX(0.77); }
  .headline--offer .line { display: block; margin-bottom: 4px; }

  .brand-badge {
    position: absolute;
    left: 120px; top: 352px;
    width: 180px; height: 180px;
    border-radius: 50%;
    background: var(--ink);
    display: flex; align-items: center; justify-content: center;
    text-align: center;
  }
  .brand-badge__name {
    font-family: "Roboto Condensed", "Arial Narrow", sans-serif;
    font-weight: 700;
    font-size: 22px;
    letter-spacing: 3px;
    line-height: 1.2;
    color: var(--logo-text);
    text-transform: uppercase;
  }

  .services {
    position: absolute;
    left: 112px; top: 786px;
    font-family: "Roboto Condensed", "Arial Narrow", sans-serif;
    font-weight: 700;
    font-size: 27.5px;
    line-height: 34px;
    text-transform: uppercase;
    white-space: nowrap;
  }

  .call-to-action {
    position: absolute;
    left: 108px; top: 898px;
    font-family: "League Gothic", "Oswald", sans-serif;
    font-size: 92px;
    line-height: 0.76;
    text-transform: uppercase;
    transform: scaleX(0.73);
    transform-origin: left top;
    white-space: nowrap;
  }

  .contact {
    position: absolute;
    left: 111px;
    white-space: nowrap;
  }
  .contact--phone {
    top: 1041px;
    font-family: "Roboto Condensed", "Arial Narrow", sans-serif;
    font-weight: 700;
    font-size: 30px;
  }
  .contact--email {
    top: 1077px;
    font-family: "Roboto", Arial, sans-serif;
    font-weight: 300;
    font-size: 29px;
    letter-spacing: 2.4px;
  }

  .vine-ornament {
    position: absolute;
    left: 548px; top: 115px;
    width: 212px; height: 775px;
    border-radius: 24px;
    background: linear-gradient(200deg, var(--ink-soft), var(--ink-faint));
  }
  .cup-illustration {
    position: absolute;
    left: 548px; top: 930px;
    width: 212px; height: 135px;
    border-radius: 24px;
    background: linear-gradient(180deg, var(--ink-soft), var(--ink-faint));
  }
</style>
</head>
<body>
  <h1 class="headline headline--intro">
    <span class="line">Did you</span>
    <span class="line">know</span>
  </h1>

  <div class="brand-badge">
    <span class="brand-badge__name">Sunny<br>Ladle</span>
  </div>

  <h2 class="headline headline--offer">
    <span class="line">Does</span>
    <span class="line">Catering?</span>
  </h2>

  <p class="services">We offer breakfast,<br>lunch and morning and<br>afternoon tea options</p>

  <p class="call-to-action">Come in store<br>to enquire</p>

  <p class="contact contact--phone">Phone 0487 602 914</p>
  <p class="contact contact--email">email:tam@sunnyladlecanteen.com</p>

  <div class="vine-ornament" role="img" aria-label="Decorative curling vine ornament with leaves trailing down toward the cup"></div>
  <div class="cup-illustration" role="img" aria-label="Coffee cup illustration with a heart"></div>
</body>
</html>
```